Criminal Defense Law Firm needs Stationary design Theme for a Business Card, Envelope, and Letterhea

Our Law Firm is seeking a general design concept for a business card, letterhead, and Envelope.

Our website is QuillmoreAdvocates.com

A design for these three items is requested to keep branding in place for the firm. Would like to keep the Firm Colors on the website consistent with our branding on business cards, letterheads, and mailing envelopes #10 size to be exact.

We would like business cards printed front and back with Law firm Colors from website.

Letterhead with law firm colors as well. Design is not limited to just the header, but the footer can be utilized as well for email, website, phone, fax, etc.

Simple #10 envelope consisting of the same design principles set out in the previous two designs.

```html
<!DOCTYPE html>
<html lang="en">
<head>
<meta charset="utf-8">
<title>Quillmore Criminal Law Offices — Letterhead</title>
<link rel="stylesheet" href="https://fonts.googleapis.com/css2?family=Crimson+Pro:wght@500&family=Lato:wght@300;400&display=swap">
<style>
  :root {
    --teal: #00a3b4;
    --gold: #a39265;
    --paper: #ffffff;
    --page-edge: #d6d6d6;
    --ghost: #f2f2f2;
    --white: #ffffff;
  }
  html, body {
    margin: 0;
    padding: 0;
    width: 939px;
    height: 1200px;
    overflow: hidden;
    background: var(--paper);
  }
  .letterhead {
    position: relative;
    width: 939px;
    height: 1200px;
    overflow: hidden;
  }
  .page-frame {
    position: absolute;
    left: 28px;
    top: 28px;
    width: 882px;
    height: 1152px;
    border: 1px solid var(--page-edge);
    box-sizing: border-box;
    overflow: hidden;
  }
  .ghost-ring {
    position: absolute;
    left: 0;
    top: 0;
  }
  .brand-block {
    position: absolute;
    left: 62px;
    top: 30px;
    width: 419px;
    height: 112px;
    background: var(--teal);
    display: flex;
    align-items: center;
    box-sizing: border-box;
    padding-left: 24px;
  }
  .brand-dot {
    width: 52px;
    height: 52px;
    border: 2px solid var(--white);
    border-radius: 50%;
    flex: none;
    margin-right: 20px;
  }
  .brand-name {
    margin: 0;
    font-family: "Crimson Pro", Georgia, serif;
    font-weight: 500;
    font-size: 23px;
    line-height: 26px;
    letter-spacing: 0.04em;
    text-transform: uppercase;
    color: var(--white);
  }
  .contact-band {
    position: absolute;
    left: 28px;
    top: 1087px;
    width: 884px;
    height: 93px;
    background: var(--gold);
    color: var(--white);
    font-family: "Lato", Arial, sans-serif;
    text-align: center;
    box-sizing: border-box;
    padding-top: 6px;
  }
  .contact-web {
    font-weight: 300;
    font-size: 32px;
    line-height: 36px;
    margin: 0;
  }
  .contact-address,
  .contact-phone {
    font-weight: 400;
    font-size: 15px;
    line-height: 20px;
    margin: 0;
  }
  .contact-phone {
    display: flex;
    justify-content: center;
    align-items: center;
    gap: 3px;
  }
  .phone-icon {
    width: 14px;
    height: 14px;
  }
</style>
</head>
<body>
  <main class="letterhead">
    <div class="page-frame">
      <svg class="ghost-ring" width="882" height="1152" viewBox="0 0 882 1152" aria-hidden="true">
        <circle cx="479" cy="593" r="462" fill="none" stroke="var(--ghost)" stroke-width="28"/>
      </svg>
    </div>

    <header class="brand-block">
      <span class="brand-dot" aria-hidden="true"></span>
      <h1 class="brand-name">Quillmore Criminal<br>Law Offices</h1>
    </header>

    <footer class="contact-band">
      <p class="contact-web">www.quillmoreadvocates.com</p>
      <p class="contact-address">2417 Larkspur Avenue NW, Alder Falls, NM 87190</p>
      <p class="contact-phone">
        <svg class="phone-icon" viewBox="0 0 16 16" aria-hidden="true">
          <circle cx="8" cy="8" r="8" fill="var(--white)"/>
          <path d="M5.2 3.8c.3-.2.7-.1.9.2l.9 1.5c.2.3.1.6-.1.8l-.6.5c.4.9 1.1 1.7 2 2.2l.5-.6c.2-.2.6-.3.8-.1l1.5.9c.3.2.4.6.2.9l-.5.8c-.3.5-.9.7-1.5.5C7 10.7 5.3 9 4.5 6.9c-.2-.6 0-1.2.5-1.5z" fill="var(--gold)"/>
        </svg>
        555.014.2890
      </p>
    </footer>
  </main>
</body>
</html>
```